Multi brand diverse distributor requires new business card

We're a distributor representing multiple brands and would like a new business card reflecting our diversity.

We incorporate landscape architecture, environmental engineering and sustainability into construction projects.

KV Group is the company name, and therefore the KV logo should be the primary logo.

Target Market(s)

Engineers, Landscape Architects, Environmental

Contact Information for Business Card

See sample

Colors

Designer to choose colors to be used in the design.

```html
<!DOCTYPE html>
<html lang="en">
<head>
<meta charset="utf-8">
<title>KV Group – Business Card</title>
<link rel="stylesheet" href="https://fonts.googleapis.com/css2?family=Montserrat:wght@400;500;600;700;800&display=swap">
<style>
  :root {
    --backdrop: #3b3b3d;
    --card: #1b1b1d;
    --card-deep: #141416;
    --red: #c8213f;
    --white: #f2f2f2;
    --grey: #bdbdbf;
    --badge-blue: #2a7fc4;
    --badge-steel: #8fa3b8;
  }
  * { box-sizing: border-box; margin: 0; padding: 0; }
  html, body { width: 1200px; height: 801px; overflow: hidden; }
  body {
    background: var(--backdrop);
    font-family: "Montserrat", sans-serif;
    position: relative;
  }
  .card {
    position: absolute;
    top: 238px;
    width: 530px;
    height: 324px;
    background: var(--card);
    border-bottom: 3px solid var(--red);
    box-shadow: 0 10px 28px rgba(0,0,0,.45);
    overflow: hidden;
  }
  .card--front { left: 50px; }
  .card--back { left: 620px; }

  /* Front */
  .brand {
    position: absolute;
    top: 26px;
    right: 30px;
    text-align: right;
  }
  .brand__name {
    color: var(--red);
    font-weight: 800;
    font-size: 58px;
    line-height: 1;
    letter-spacing: 1px;
  }
  .brand__group {
    color: var(--white);
    font-weight: 600;
    font-size: 13px;
    letter-spacing: 11px;
    margin-top: 6px;
    margin-right: -11px;
  }
  .brand__rule {
    height: 1px;
    background: var(--red);
    margin-top: 6px;
  }
  .brand__est {
    color: var(--white);
    font-size: 10px;
    letter-spacing: 3px;
    margin-top: 6px;
  }
  .divider {
    position: absolute;
    left: 0;
    right: 30px;
    top: 168px;
    height: 1px;
    background: var(--red);
  }
  .person {
    position: absolute;
    left: 30px;
    top: 188px;
  }
  .person__name {
    color: var(--red);
    font-weight: 700;
    font-size: 17px;
    letter-spacing: .5px;
  }
  .person__title {
    color: var(--white);
    font-size: 12px;
    margin-top: 3px;
  }
  .contact {
    list-style: none;
    margin-top: 14px;
  }
  .contact li {
    display: flex;
    align-items: center;
    gap: 8px;
    color: var(--white);
    font-size: 12.5px;
    line-height: 19px;
  }
  .contact svg { width: 11px; height: 11px; flex: none; }
  .partners {
    position: absolute;
    right: 30px;
    top: 188px;
    text-align: right;
  }
  .partners__badges {
    display: flex;
    justify-content: flex-end;
    gap: 14px;
    align-items: center;
  }
  .badge--bars { width: 70px; height: 22px; background: var(--badge-steel); }
  .badge--oval { width: 62px; height: 30px; border-radius: 50%; background: var(--badge-blue); }
  .cities {
    color: var(--white);
    font-size: 13px;
    line-height: 20px;
    margin-top: 14px;
  }
  .cities .dot { color: var(--red); margin: 0 4px; }

  /* Back */
  .pattern {
    position: absolute;
    inset: 0;
    background: linear-gradient(135deg, #161618 0%, #232325 55%, #2c2c2e 100%);
  }
  .back-brand {
    position: absolute;
    right: 32px;
    bottom: 48px;
    text-align: right;
  }
  .back-brand__est {
    color: var(--white);
    font-size: 9px;
    letter-spacing: 3px;
    margin-bottom: 4px;
  }
  .back-brand__name {
    color: var(--red);
    font-weight: 800;
    font-size: 40px;
    line-height: 1;
    letter-spacing: 1px;
  }
  .back-brand__rule {
    height: 1px;
    background: var(--red);
    margin-top: 6px;
    width: 250px;
    margin-left: auto;
  }
</style>
</head>
<body>

<section class="card card--front" aria-label="Business card front">
  <div class="brand">
    <div class="brand__name">KV</div>
    <div class="brand__group">GROUP</div>
    <div class="brand__rule"></div>
    <div class="brand__est">EST. 1971</div>
  </div>

  <div class="divider"></div>

  <div class="person">
    <div class="person__name">MARCO VENTURI</div>
    <div class="person__title">B.Eng (Civil)</div>
    <ul class="contact">
      <li>
        <svg viewBox="0 0 12 12" aria-hidden="true"><path fill="var(--red)" d="M2.5 1l2 2.2-1 1.3c.7 1.5 1.8 2.6 3.3 3.3l1.3-1 2.2 2-1.1 1.7C5 10.3 1.7 7 .8 2.1z"/></svg>
        0400 123 456
      </li>
      <li>
        <svg viewBox="0 0 12 12" aria-hidden="true"><rect x="3" y="1" width="6" height="10" rx="1" fill="none" stroke="var(--white)" stroke-width="1.2"/></svg>
        1300 555 019
      </li>
      <li>
        <svg viewBox="0 0 12 12" aria-hidden="true"><rect x="1" y="2.5" width="10" height="7" fill="var(--red)"/><path d="M1 2.5l5 4 5-4" fill="none" stroke="var(--card)" stroke-width="1"/></svg>
        marco@kv.com.au
      </li>
      <li>
        <svg viewBox="0 0 12 12" aria-hidden="true"><circle cx="6" cy="6" r="5" fill="var(--red)"/><path d="M1 6h10M6 1c-2 2.5-2 7.5 0 10M6 1c2 2.5 2 7.5 0 10" fill="none" stroke="var(--card)" stroke-width=".8"/></svg>
        www.kv.com.au
      </li>
    </ul>
  </div>

  <div class="partners">
    <div class="partners__badges">
      <div class="badge--bars" role="img" aria-label="Partner brand badge"></div>
      <div class="badge--oval" role="img" aria-label="Partner brand badge"></div>
    </div>
    <div class="cities">
      Adelaide<span class="dot">•</span>Brisbane<br>
      Melbourne<span class="dot">•</span>Perth<span class="dot">•</span>Sydney
    </div>
  </div>
</section>

<section class="card card--back" aria-label="Business card back">
  <div class="pattern" role="img" aria-label="Tone-on-tone repeating monogram pattern"></div>
  <div class="back-brand">
    <div class="back-brand__est">EST. 1971</div>
    <div class="back-brand__name">KV GROUP</div>
    <div class="back-brand__rule"></div>
  </div>
</section>

</body>
</html>
```